New Business Card Design Project

I need a meaningful new business card. Therefore, the website should convey growth, joy, uniqueness, workout and a bit of luxury.
Color scheme should be petrol, gold and matching colors.

```html
<!DOCTYPE html>
<html lang="en">
<head>
<meta charset="utf-8">
<title>Verdance Pilates – Business Card</title>
<link href="https://fonts.googleapis.com/css2?family=Poppins:wght@400;500&family=Great+Vibes&display=swap" rel="stylesheet">
<style>
  :root {
    --stage: #c9c9c9;
    --petrol: #19aa9d;
    --petrol-deep: #128f84;
    --petrol-faint: #dcf2ef;
    --gold: #c9a44c;
    --gold-soft: #e2c67f;
    --paper: #ffffff;
    --ink: #2f2f33;
    --ink-soft: #4a4a55;
    --web-blue: #4b5b8c;
  }
  * { box-sizing: border-box; margin: 0; padding: 0; }
  html, body { width: 1200px; height: 900px; overflow: hidden; }
  body {
    background: var(--stage);
    font-family: "Poppins", sans-serif;
    position: relative;
  }
  .card {
    position: absolute;
    left: 250px;
    width: 700px;
    height: 400px;
    border-radius: 34px;
    overflow: hidden;
    box-shadow: 0 6px 18px rgba(0,0,0,0.25);
  }
  .card--front { top: 40px; background: var(--petrol); }
  .card--back { top: 470px; background: var(--paper); }

  .figure-art {
    position: absolute;
    border-radius: 50% 50% 40% 40%;
  }
  .card--front .figure-art {
    right: 30px; top: 20px; width: 280px; height: 360px;
    background: linear-gradient(160deg, rgba(255,255,255,0.16), rgba(255,255,255,0.04));
  }
  .card--back .figure-art {
    right: 30px; top: 20px; width: 300px; height: 360px;
    background: linear-gradient(160deg, #eef8f7, #f6fbfa 70%, rgba(255,255,255,0));
  }

  /* front identity */
  .front-identity {
    position: absolute;
    left: 90px; top: 120px; width: 360px;
    display: flex; flex-direction: column; align-items: center;
  }
  .brand {
    display: flex;
    align-items: center;
    gap: 12px;
    font-weight: 500;
    white-space: nowrap;
  }
  .brand__dot { width: 22px; height: 22px; border-radius: 50%; background: var(--gold); flex: none; }
  .card--front .brand { font-size: 40px; color: var(--paper); }
  .gold-rule {
    height: 2px; background: var(--gold-soft); border-radius: 1px;
  }
  .card--front .gold-rule { width: 220px; margin-top: 16px; }
  .card--front .tagline {
    margin-top: 12px; font-size: 15px; letter-spacing: 6px; text-transform: uppercase;
    color: var(--paper);
  }

  /* back identity */
  .back-identity {
    position: absolute; left: 48px; top: 100px;
  }
  .card--back .brand { font-size: 28px; color: var(--petrol); }
  .card--back .gold-rule { width: 160px; margin-top: 12px; margin-left: 34px; background: var(--gold); }

  .person {
    position: absolute; right: 60px; top: 62px; text-align: right;
  }
  .person__name {
    font-family: "Great Vibes", cursive;
    font-size: 46px; color: var(--petrol); line-height: 1.1;
  }
  .person__role {
    font-size: 18px; color: var(--ink-soft); margin-top: 2px;
  }
  .person .gold-rule { width: 90px; margin: 12px 0 0 auto; background: var(--gold); }
  .address {
    position: absolute; right: 60px; top: 200px; text-align: right;
    font-size: 18px; color: var(--ink-soft); line-height: 1.4;
  }
  .contacts {
    position: absolute; left: 48px; bottom: 42px;
    list-style: none; font-size: 20px; color: var(--ink); line-height: 1.5;
  }
  .contacts li { display: flex; align-items: center; gap: 10px; }
  .contacts svg { width: 18px; height: 18px; flex: none; }
  .contacts .web { color: var(--web-blue); }
</style>
</head>
<body>

<section class="card card--front" aria-label="Card front">
  <div class="figure-art" role="img" aria-label="Faint line illustration of a woman in a pilates pose"></div>
  <div class="front-identity">
    <div class="brand"><span class="brand__dot"></span>Verdance Pilates</div>
    <div class="gold-rule"></div>
    <p class="tagline">Practice</p>
  </div>
</section>

<section class="card card--back" aria-label="Card back">
  <div class="figure-art" role="img" aria-label="Faint line illustration of a woman in a pilates pose"></div>
  <div class="back-identity">
    <div class="brand"><span class="brand__dot"></span>Verdance Pilates</div>
    <div class="gold-rule"></div>
  </div>

  <div class="person">
    <p class="person__name">Elena Marlowe</p>
    <p class="person__role">Managing Director</p>
    <div class="gold-rule"></div>
  </div>

  <p class="address">18, Linden Row Suite 4<br>30219, Maple Harbor</p>

  <ul class="contacts">
    <li>
      <svg viewBox="0 0 24 24" aria-hidden="true"><path fill="var(--petrol)" d="M6.6 10.8a15 15 0 0 0 6.6 6.6l2.2-2.2a1 1 0 0 1 1-.25 11.4 11.4 0 0 0 3.6.57 1 1 0 0 1 1 1V20a1 1 0 0 1-1 1A17 17 0 0 1 3 4a1 1 0 0 1 1-1h3.5a1 1 0 0 1 1 1c0 1.25.2 2.45.57 3.570a1 1 0 0 1-.25 1z"/></svg>
      021-555 808 314
    </li>
    <li>
      <svg viewBox="0 0 24 24" aria-hidden="true"><rect x="2" y="5" width="20" height="14" rx="1" fill="var(--petrol)"/><path d="M2 6l10 7 10-7" fill="none" stroke="#fff" stroke-width="1.6"/></svg>
      hello@verdancepilates.com
    </li>
    <li>
      <svg viewBox="0 0 24 24" aria-hidden="true"><circle cx="12" cy="12" r="10" fill="none" stroke="var(--petrol)" stroke-width="2"/><path d="M2 12h20M12 2c3 3 3 17 0 20M12 2c-3 3-3 17 0 20" fill="none" stroke="var(--petrol)" stroke-width="1.6"/></svg>
      <span>www.<span class="web">verdancepilates</span>.com</span>
    </li>
  </ul>
</section>

</body>
</html>
```